high end contractor

high end contracting company we do all phases of construction kitchen,bathrooms,etc... please look at my website before you design www.harborlinebld.com

would love some sort of lines or logo or both

Industry/Entity Type

Construction

Contact Information for Business Card

company name: harbor & lantern contracting address: 412 birchwood ave Eastbrook Ny 10599 email: harborlinebld@mailzone.com website: www.harborlinebld.com office#: 914-555-0182 fax#: 914-555-0197 dominic fersalo mobile# 917-555-0263

```html
<!DOCTYPE html>
<html lang="en">
<head>
<meta charset="utf-8">
<title>Harbor &amp; Lantern Contracting – Business Card Concepts</title>
<link rel="stylesheet" href="https://fonts.googleapis.com/css2?family=Sorts+Mill+Goudy&display=swap">
<style>
  :root {
    --teal: #14a89e;
    --teal-light: #4fc3c8;
    --charcoal: #545454;
    --ink: #5e5e5e;
    --paper: #ffffff;
    --paper-grey: #efefef;
    --serif: "Sorts Mill Goudy", Georgia, serif;
  }
  * { box-sizing: border-box; margin: 0; padding: 0; }
  html, body { width: 1200px; height: 949px; overflow: hidden; background: var(--paper); }
  body { position: relative; font-family: var(--serif); color: var(--ink); font-variant-numeric: lining-nums; }

  .card { position: absolute; overflow: hidden; }
  .abs { position: absolute; white-space: nowrap; }
  .icon { width: 11px; height: 11px; vertical-align: -1px; margin-right: 6px; }
  .teal-label { color: var(--teal); }

  /* Card one: vertical teal band */
  .card--band { left: 77px; top: 129px; width: 482px; height: 313px; background: var(--paper-grey); border: 1px solid #444; }
  .card--band .band { left: 70px; width: 162px; background: var(--teal); }
  .card--band .band--top { top: 0; height: 77px; }
  .card--band .band--bottom { top: 188px; height: 125px; }
  .card--band .rule { top: 155px; height: 5px; background: var(--teal); }
  .card--band .brand { left: 42px; top: 136px; width: 220px; text-align: center; font-size: 23px; }
  .card--band .web { left: 70px; top: 191px; width: 162px; text-align: center; color: #fff; font-size: 10.5px; }
  .card--band .name { left: 280px; top: 98px; font-size: 20px; }
  .card--band .email { left: 282px; top: 120px; font-size: 10px; }
  .card--band .phone { left: 282px; top: 136px; font-size: 11.5px; }
  .card--band .address { left: 283px; top: 168px; font-size: 9.5px; }
  .card--band .lines { left: 283px; top: 182px; font-size: 8px; display: flex; gap: 20px; }

  /* Card two: patterned top & bottom */
  .card--pattern { left: 70px; top: 527px; width: 476px; height: 293px; background: var(--paper); border: 1px solid #333; }
  .card--pattern .pattern { left: 0; width: 100%; background: linear-gradient(90deg, #e4e4e4 0%, #9fd3cf 35%, #e8e8e8 55%, #7ecfd0 75%, #e6e6e6 100%); }
  .card--pattern .pattern--top { top: 0; height: 74px; }
  .card--pattern .pattern--bottom { top: 216px; height: 77px; background: linear-gradient(90deg, #3aa3a0 0%, #e8e8e8 40%, #8fc9c6 75%, #eeeeee 100%); }
  .card--pattern .bar { top: 198px; left: 0; width: 100%; height: 18px; background: var(--charcoal); color: #fff; font-size: 9.5px; display: flex; align-items: center; gap: 12px; padding-left: 14px; }
  .card--pattern .dot { width: 6px; height: 6px; background: var(--teal-light); transform: rotate(45deg); }
  .card--pattern .brand { left: 18px; top: 150px; width: 230px; text-align: center; font-size: 24px; }
  .card--pattern .web { left: 92px; top: 176px; font-size: 10.5px; color: var(--teal-light); }
  .card--pattern .name { left: 280px; top: 99px; font-size: 24px; }
  .card--pattern .email { left: 281px; top: 126px; font-size: 12px; }
  .card--pattern .phone { left: 281px; top: 145px; font-size: 13.5px; }

  /* Card three: dark name band */
  .card--dark { left: 684px; top: 306px; width: 486px; height: 317px; background: #f7f8f9; border-top: 1px solid #444; border-right: 1px solid #444; }
  .card--dark .facets { left: 0; top: 0; width: 220px; height: 217px; background: linear-gradient(90deg, #0a8f95 0%, #14b0b8 40%, #9fdde0 75%, rgba(247,248,249,0) 100%); }
  .card--dark .brand { left: 185px; top: 117px; width: 260px; text-align: center; font-size: 27px; }
  .card--dark .web { right: 49px; top: 146px; font-size: 11px; color: var(--teal-light); }
  .card--dark .address { right: 49px; top: 161px; font-size: 11px; }
  .card--dark .lines { right: 49px; top: 175px; font-size: 9px; display: flex; gap: 24px; }
  .card--dark .nameband { left: 0; top: 217px; width: 100%; height: 100px; background: var(--charcoal); color: #fff; }
  .card--dark .name-row { position: absolute; top: 6px; left: 0; width: 100%; display: flex; align-items: center; gap: 10px; }
  .card--dark .double-rule { flex: 1; height: 7px; border-top: 3px solid var(--teal-light); border-bottom: 2px solid var(--teal-light); }
  .card--dark .name { font-size: 30px; white-space: nowrap; }
  .card--dark .contact-row { position: absolute; top: 47px; left: 0; width: 100%; display: flex; justify-content: center; gap: 30px; font-size: 15px; }
  .card--dark .icon { width: 16px; height: 16px; margin-right: 8px; vertical-align: -2px; }
</style>
</head>
<body>

<svg width="0" height="0" style="position:absolute">
  <symbol id="i-mail" viewBox="0 0 16 12"><rect x="0.75" y="0.75" width="14.5" height="10.5" fill="none" stroke="#4fc3c8" stroke-width="1.3"/><path d="M1 1l7 6 7-6" fill="none" stroke="#4fc3c8" stroke-width="1.3"/></symbol>
  <symbol id="i-phone" viewBox="0 0 10 16"><rect x="0.75" y="0.75" width="8.5" height="14.5" rx="1.5" fill="none" stroke="#4fc3c8" stroke-width="1.3"/><line x1="3.5" y1="12.8" x2="6.5" y2="12.8" stroke="#4fc3c8" stroke-width="1.3"/></symbol>
</svg>

<section class="card card--band">
  <div class="abs band band--top"></div>
  <div class="abs band band--bottom"></div>
  <div class="abs rule" style="left:0;width:35px"></div>
  <div class="abs rule" style="left:281px;width:129px"></div>
  <div class="abs rule" style="left:430px;width:52px"></div>
  <div class="abs brand">Harbor &amp; Lantern</div>
  <div class="abs web">www.harborlinebld.com</div>
  <div class="abs name">Dominic Fersalo</div>
  <div class="abs email"><svg class="icon"><use href="#i-mail"/></svg>harborlinebld@mailzone.com</div>
  <div class="abs phone"><svg class="icon"><use href="#i-phone"/></svg>917-555-0263</div>
  <div class="abs address">412 Birchwood Ave Eastbrook Ny 10599</div>
  <div class="abs lines"><span><span class="teal-label">Office :</span> 914-555-0182</span><span><span class="teal-label">Fax :</span> 914-555-0197</span></div>
</section>

<section class="card card--pattern">
  <div class="abs pattern pattern--top" role="img" aria-label="Grey and teal diamond pattern"></div>
  <div class="abs brand">Harbor &amp; Lantern</div>
  <div class="abs web">www.harborlinebld.com</div>
  <div class="abs name">Dominic Fersalo</div>
  <div class="abs email"><svg class="icon"><use href="#i-mail"/></svg>harborlinebld@mailzone.com</div>
  <div class="abs phone"><svg class="icon"><use href="#i-phone"/></svg>917-555-0263</div>
  <div class="abs bar">
    <span>412 Birchwood Ave Eastbrook Ny 10599</span><span class="dot"></span>
    <span>Office : 914-555-0182</span><span class="dot"></span>
    <span>Fax : 914-555-0197</span>
  </div>
  <div class="abs pattern pattern--bottom" role="img" aria-label="Grey and teal diamond pattern"></div>
</section>

<section class="card card--dark">
  <div class="abs facets" role="img" aria-label="Teal triangular facet pattern fading to white"></div>
  <div class="abs brand">Harbor &amp; Lantern</div>
  <div class="abs web">www.harborlinebld.com</div>
  <div class="abs address">412 Birchwood Ave Eastbrook Ny 10599</div>
  <div class="abs lines"><span><span class="teal-label">Office :</span> 914-555-0182</span><span><span class="teal-label">Fax :</span> 914-555-0197</span></div>
  <div class="abs nameband">
    <div class="name-row"><span class="double-rule"></span><span class="name">Dominic Fersalo</span><span class="double-rule"></span></div>
    <div class="contact-row">
      <span><svg class="icon"><use href="#i-mail"/></svg>harborlinebld@mailzone.com</span>
      <span><svg class="icon"><use href="#i-phone"/></svg>917-555-0263</span>
    </div>
  </div>
</section>

</body>
</html>
```